Energy Company 8-page Brochure

We are in need of a redesign of our 8-page brochure. Attached is the initial design that does not represent us very well. We are looking for CLEAN/CORPORATE look with a little bit of flair (graphs/charts if applicable).

I prefer white background and our company colors (blue/green) to be the accent colors. Feel free to add additional accent colors to highlight certain areas.

We are in the energy field (not just solar), so please consider the types of images that you will use. Are headquarters is located in Chicago, IL so a great looking picture of the skyline or something similar would work for the front and back cover.

We have additional marketing collateral that we will want to be uniformed once we have the right design.

Good luck, and we look forward to receiving some great designs!

Best Regards,
Rob

Target Market(s)

Small to large businesses (B2B).

Industry/Entity Type

It Company

Colors
ffffff
9bcb3c
0255a3

Requirements
Must have
• Clean design, company colors, specified content and editable files.
Nice to have
• Graphs, charts, highlighted areas where necessary.
Should not have
• Clutter! Please utilized page space appropriately. There is a lot of content, so you need to consider graphics and image placement.

```html
<!DOCTYPE html>
<html lang="en">
<head>
<meta charset="utf-8">
<title>Brightline Energy Brochure Spread</title>
<link href="https://fonts.googleapis.com/css2?family=Open+Sans:wght@300;400;600;700&display=swap" rel="stylesheet">
<style>
:root{
  --blue:#0255a3;
  --blue-deep:#1f4f86;
  --green:#6aa532;
  --green-text:#4f8a1f;
  --green-ring:#9bcb3c;
  --ink:#555b61;
  --paper:#ffffff;
  --stage:#e4e5e6;
}
*{box-sizing:border-box;margin:0;padding:0}
html,body{width:1200px;height:800px;overflow:hidden;background:var(--stage);font-family:"Open Sans",Arial,sans-serif}
.spread{position:absolute;left:50px;top:50px;width:1100px;height:700px;display:flex;box-shadow:0 6px 24px rgba(0,0,0,.18)}
.page{position:relative;width:550px;height:700px;background:var(--paper);overflow:hidden}
.page--left{background:linear-gradient(90deg,#fff 85%,#f0f1f2 100%)}
.page--right{background:linear-gradient(90deg,#eceded 0%,#fff 12%)}
.skyline-photo{position:absolute;left:0;top:0;width:550px;height:180px;background:linear-gradient(180deg,#6e74a8 0%,#9a8fb0 45%,#b8807a 62%,#3d3f6a 75%,#6b5a7a 100%)}
.title-box{position:absolute;left:30px;top:40px;width:190px;height:170px;background:var(--green);color:#fff;padding:28px 22px}
.title-box__kicker{font-size:14px;font-weight:300;white-space:nowrap}
.title-box__heading{font-size:30px;font-weight:400;line-height:1.1;margin-top:4px}
.stories{position:absolute;left:55px;top:250px;list-style:none;width:440px}
.story{display:flex;align-items:center;height:70px;margin-bottom:4px}
.badge{flex:none;width:58px;height:58px;border-radius:50%;display:flex;flex-direction:column;align-items:center;justify-content:center;color:#fff;font-weight:700;font-size:17px;line-height:1}
.badge small{font-size:11px;margin-top:2px}
.badge--blue{background:var(--blue);border:4px solid #9fc0e0}
.badge--green{background:var(--green);border:4px solid #c6e29a}
.story__text{margin-left:12px;font-size:12px;color:var(--ink);line-height:1.45}
.story__lead{color:var(--blue);text-transform:uppercase}
.building-photo{position:absolute;left:0;top:0;width:550px;height:320px;background:linear-gradient(160deg,#8fb0d6 0%,#3f6fa6 45%,#1e4f86 100%)}
.mission{position:absolute;left:45px;top:195px;color:#fff}
.mission__kicker{font-size:13px;font-weight:300;text-transform:uppercase}
.mission__heading{font-size:28px;font-weight:300;line-height:1.05}
.brand{position:absolute;left:45px;top:445px;display:flex;align-items:center;gap:8px;color:#6b7380;font-size:15px}
.brand__mark{width:22px;height:22px;background:#9fb6cf}
.pledge{position:absolute;left:45px;top:490px;width:165px;color:var(--blue-deep);font-weight:700;font-size:13px;line-height:1.35}
.column{position:absolute;top:345px;width:152px;color:var(--green-text);font-size:11.5px;line-height:1.4}
.column--one{left:212px}
.column--two{left:374px}
.column strong{text-transform:uppercase;font-weight:700}
.column p+p{margin-top:16px}
</style>
</head>
<body>
<div class="spread">
  <section class="page page--left">
    <div class="skyline-photo" role="img" aria-label="City skyline at dusk reflected on the lakefront"></div>
    <div class="title-box">
      <p class="title-box__kicker">Lower energy cost</p>
      <h1 class="title-box__heading">Success Stories</h1>
    </div>
    <ul class="stories">
      <li class="story"><span class="badge badge--blue">$<small>400,000</small></span><p class="story__text"><span class="story__lead">3 year savings</span> for early learning centers by securing a low rate per kilowatt hour (kWh) for their electricity</p></li>
      <li class="story"><span class="badge badge--green">50%</span><p class="story__text"><span class="story__lead">50% savings</span> for manufacturing firm by upgrading to LED lighting</p></li>
      <li class="story"><span class="badge badge--blue">27%</span><p class="story__text"><span class="story__lead">27% energy usage</span> reduction by implementing our Q Series lighting controls for an Apex 100 company</p></li>
      <li class="story"><span class="badge badge--green">$<small>200,000</small></span><p class="story__text"><span class="story__lead">Savings for</span> restaurant group on their electricity bills by competitive supplier bidding</p></li>
      <li class="story"><span class="badge badge--blue">30%</span><p class="story__text"><span class="story__lead">30% annual savings</span> for Distribution Center through lighting retrofit and HVAC controls</p></li>
      <li class="story"><span class="badge badge--green">25%</span><p class="story__text"><span class="story__lead">25% reduction</span> in water usage for a property management company for their multi-unit buildings</p></li>
    </ul>
  </section>
  <section class="page page--right">
    <div class="building-photo" role="img" aria-label="Glass office towers seen from below, tinted blue"></div>
    <div class="mission">
      <p class="mission__kicker">Our mission</p>
      <h2 class="mission__heading">We help our clients<br>lower their energy costs</h2>
    </div>
    <div class="brand"><span class="brand__mark"></span><span>Summit Crest</span></div>
    <p class="pledge">Brightline Energy and its partner company, K2-Kinetic Efficiency Partners, are dedicated to helping you lower your company's operating expenses.</p>
    <div class="column column--one">
      <p><strong>Brightline Energy and K2</strong> are operating divisions of Summit Crest Holdings, a publicly traded energy services company. As a vendor-independent company, there are many ways in which we help you lower your energy expenditures. Brightline Energy (BLE) lowers the cost of energy through competitive supplier bidding and K2 creates comprehensive energy savings solutions through the implementation of energy reduction services.</p>
    </div>
    <div class="column column--two">
      <p><strong>Our diverse portfolio</strong> of leading competitive energy suppliers, comprehensive energy efficiency solutions, best-in-class products, and unparalleled industry experience provide our clients with the confidence that they are getting the best solutions for their energy needs.</p>
      <p><strong>By reducing the price</strong> for energy and lowering usage, BLE and K2 allow businesses to keep more of their own capital.</p>
    </div>
  </section>
</div>
</body>
</html>
```